Larkfield Rowhomes - Billboard design for our newly renovated townhome community

We have a 5' wide x 4' tall billboard at the entrance to our apartment community, that needs to have the acrylic insert replaced. It is a 2 sided sign, and we are planning to use the same image on both sides. We are called Larkfield Rowhomes, and have 48 townhomes that are all 2 bedroom, 1 1/2 bath. A few things we would like to get across on the signage: "Newly Renovated" "2 bed 1 1/2 bath" "Full size W/D in every home" " New Appliances" I've included our parent company's logo - this is the only image I could think of, but it might not be worth having it on the sign. We are in Colorado, so mountain theme could be nice and also sunshine/sun since we are called "Larkfield"

Industry/Entity Type

Apartment

Font styles to use
Sans Serif

Requirements
Must have
• Newly Renovated
2 bed 1 1/2 bath
Full size W/D in every home
Virtual Tours available
www.brambletonhomesco.example
855 - 413 - 9286
Nice to have
• We are located in Colorado - possibly mountain theme? Since our community is called "Larkfield Rowhomes" - anything bright with Sun / Sunshine might look really nice as well.

```html
<!DOCTYPE html>
<html lang="en">
<head>
<meta charset="utf-8">
<title>Larkfield Rowhomes – Entrance Sign</title>
<link rel="stylesheet" href="https://fonts.googleapis.com/css2?family=Anton&family=Oswald:wght@500;600&display=swap">
<style>
  :root {
    --backdrop: #dcdadb;
    --sign-red: #e8222a;
    --sign-yellow: #fbd10a;
    --badge-purple: #5b2a6e;
    --ink-black: #141414;
    --panel-white: #ffffff;
    --panel-ink: #4a4a4a;
    --sky-top: #6f98d2;
    --sky-cloud: #e6edf4;
    --land-tan: #b5ab8a;
    --land-green: #8f9670;
  }
  html, body {
    margin: 0;
    padding: 0;
    width: 1200px;
    height: 533px;
    overflow: hidden;
    background: var(--backdrop);
  }
  .canvas {
    position: relative;
    width: 1200px;
    height: 533px;
  }
  .sign {
    position: absolute;
    left: 287px;
    top: 16px;
    width: 625px;
    height: 500px;
    overflow: hidden;
    background: var(--panel-white);
  }
  .scenery {
    position: absolute;
    inset: 0;
    background: linear-gradient(180deg,
      var(--sky-top) 0%,
      #a9c2e2 18%,
      var(--sky-cloud) 36%,
      #d9dccf 46%,
      var(--land-tan) 58%,
      #a8a685 74%,
      var(--land-green) 100%);
  }
  .brand-panel {
    position: absolute;
    top: 0;
    right: 0;
    width: 303px;
    height: 167px;
  }
  .brand-panel svg { position: absolute; inset: 0; }
  .brand-name {
    position: absolute;
    left: 80px;
    right: 0;
    top: 0;
    height: 167px;
    display: flex;
    align-items: center;
    justify-content: center;
    font-family: "Oswald", sans-serif;
    font-weight: 500;
    font-size: 24px;
    color: var(--panel-ink);
    letter-spacing: 0.5px;
  }
  .tour-badge {
    position: absolute;
    left: 222px;
    top: 66px;
    width: 140px;
    height: 104px;
  }
  .tour-badge-text {
    position: absolute;
    inset: 0;
    display: flex;
    flex-direction: column;
    align-items: center;
    justify-content: center;
    transform: rotate(-14deg);
    font-family: "Oswald", sans-serif;
    font-weight: 600;
    color: #fff;
    line-height: 1;
    text-transform: uppercase;
  }
  .tour-badge-text .main { font-size: 17px; }
  .tour-badge-text .sub { font-size: 11px; font-weight: 500; margin-top: 2px; }
  .headline {
    position: absolute;
    left: 16px;
    top: 168px;
    margin: 0;
    font-family: "Anton", sans-serif;
    font-weight: 400;
    font-size: 84px;
    line-height: 0.88;
    color: var(--sign-red);
    text-transform: uppercase;
    -webkit-text-stroke: 3px var(--sign-yellow);
    paint-order: stroke fill;
    text-shadow: 4px 4px 0 var(--ink-black);
    letter-spacing: 0.5px;
  }
  .headline span { display: block; }
  .features {
    position: absolute;
    left: 0;
    top: 331px;
    width: 330px;
    height: 112px;
    background: var(--sign-yellow);
    clip-path: polygon(0 0, 262px 0, 322px 100%, 0 100%);
  }
  .features ul {
    list-style: none;
    margin: 0;
    padding: 17px 0 0 20px;
    font-family: "Oswald", sans-serif;
    font-weight: 600;
    font-size: 22px;
    line-height: 28px;
    color: var(--sign-red);
    text-transform: uppercase;
  }
  .contact-bar {
    position: absolute;
    left: 0;
    right: 0;
    bottom: 0;
    height: 57px;
    background: var(--sign-red);
    display: flex;
    align-items: center;
    justify-content: center;
    gap: 12px;
    font-family: "Oswald", sans-serif;
    font-weight: 500;
    font-size: 25px;
    color: var(--sign-yellow);
    text-transform: uppercase;
    white-space: nowrap;
  }
</style>
</head>
<body>
<main class="canvas">
  <section class="sign">
    <div class="scenery" role="img" aria-label="Photo of a Colorado alpine lake and rocky mountain slope under a blue sky with white clouds"></div>

    <div class="brand-panel">
      <svg width="303" height="167" viewBox="0 0 303 167">
        <polygon points="0,0 303,0 303,167 59,167" fill="var(--panel-white)"/>
        <polyline points="0,0 59,167 303,167" fill="none" stroke="#333" stroke-width="1.5"/>
      </svg>
      <div class="brand-name">Crestline Living</div>
    </div>

    <div class="tour-badge">
      <svg width="140" height="104" viewBox="0 0 140 104">
        <g transform="rotate(-14 70 52)">
          <rect x="20" y="20" width="112" height="64" rx="10" fill="var(--badge-purple)"/>
          <rect x="10" y="24" width="112" height="64" rx="10" fill="var(--sign-red)"/>
        </g>
      </svg>
      <div class="tour-badge-text">
        <span class="main">Virtual Tours</span>
        <span class="sub">Available</span>
      </div>
    </div>

    <h1 class="headline"><span>Larkfield</span><span>Rowhomes</span></h1>

    <div class="features">
      <ul>
        <li>Newly Renovated</li>
        <li>2 Bed 1½ Bath</li>
        <li>Full Size W/D in Every Home</li>
      </ul>
    </div>

    <footer class="contact-bar">
      <span class="web">www.brambletonhomesco.example</span>
      <span class="divider">|</span>
      <span class="phone">855 - 413 - 9286</span>
    </footer>
  </section>
</main>
</body>
</html>
```